Shopify ecommerce Custom Web page

We are using Shopify for our ecommerce system for some our products lines and we need the pages to be designed to match a new website that we are building. These pages will need to effective promote our e-learning products.

The designer will need to incorporate the design into Shopify along with the coding required to ensure the site is functional.
Updates

Reason: It was not completed by the previous bidder.

The project has been reopened and we have added an additional $200. Please response interest for those who have already bid and additionally those who have not.

Industry/Entity Type

Building

Requirements
Must have
• The shopify site needs to be functional as the deliverable for this project

```html
<!DOCTYPE html>
<html lang="en">
<head>
<meta charset="utf-8">
<title>LEARNBOX – StoryPath Assets</title>
<link href="https://fonts.googleapis.com/css2?family=Open+Sans:wght@300;400;700&family=Roboto+Condensed:wght@400;700&family=Source+Sans+3:wght@300;400&display=swap" rel="stylesheet">
<style>
:root{
  --blue:#1b9fd8;
  --blue-dark:#11719c;
  --topbar:#1b1c1e;
  --header:#9a9a9a;
  --footer:#1f1f1f;
  --footer-base:#161616;
  --text:#2a2a2a;
  --muted:#a9a9a9;
  --line:#dcdcdc;
  --white:#fff;
}
*{box-sizing:border-box;margin:0;padding:0}
html,body{width:1200px;height:1189px;overflow:hidden;background:var(--white)}
body{position:relative;font-family:"Source Sans 3",Arial,sans-serif;color:var(--text)}
.abs{position:absolute}

/* top bar */
.topbar{left:0;top:0;width:1200px;height:35px;background:var(--topbar)}
.search{left:746px;top:7px;width:156px;height:22px;background:var(--white);font-size:10px;color:#777;padding:5px 8px;font-family:Arial,sans-serif}
.search-btn{left:902px;top:7px;width:25px;height:22px;background:var(--blue)}
.cart-icon{left:940px;top:11px}
.cart-text{left:969px;top:12px;font-size:10px;color:#ccc;font-family:Arial,sans-serif}

/* header */
.header{left:0;top:35px;width:1200px;height:75px;background:var(--header)}
.logo{left:164px;top:52px;font-family:"Open Sans",sans-serif;font-weight:700;font-size:33px;color:var(--white);letter-spacing:-.5px}
.nav{right:175px;top:66px;display:flex;gap:20px;font-family:"Open Sans",sans-serif;font-weight:700;font-size:12.5px;color:var(--white)}

/* hero */
.hero{left:0;top:110px;width:1200px;height:311px;background:radial-gradient(ellipse at 30% 40%,#5a5a5a 0%,#2c2c2c 55%,#141414 100%)}
.hero-figure{left:165px;top:136px;width:300px;height:285px;background:linear-gradient(180deg,#f2f2f2,#dcdcdc);border-radius:120px 120px 0 0;opacity:.9}
.hero-title{left:544px;top:150px;font-family:"Open Sans",sans-serif;font-weight:700;font-size:27px;color:var(--white);white-space:nowrap}
.hero-text{left:545px;top:192px;width:580px;font-family:"Open Sans",sans-serif;font-size:20.5px;line-height:28.5px;color:#eee}
.hero-btn{left:547px;top:298px;width:188px;height:52px;background:var(--blue);border-bottom:4px solid var(--blue-dark);font-family:"Open Sans",sans-serif;font-weight:300;font-size:25px;color:var(--white);text-align:center;line-height:50px}
.tabs{left:165px;top:385px;display:flex;gap:7px}
.tab{height:36px;padding:0 14px;background:var(--white);font-family:"Roboto Condensed",sans-serif;font-weight:700;font-size:14.5px;line-height:38px;color:#111;position:relative;white-space:nowrap}
.tab.active{background:var(--blue);color:var(--white)}
.tab.active::after{content:"";position:absolute;left:74px;bottom:-7px;border:6px solid transparent;border-top-color:var(--blue);border-bottom:0}
.dots{left:963px;top:398px;display:flex;gap:5px}
.dot{width:12px;height:12px;border-radius:50%;background:var(--white)}
.dot.on{background:#111}

/* product */
.product-shot{left:165px;top:448px;width:348px;height:320px;border:1px solid var(--line);border-radius:3px;background:linear-gradient(180deg,#fff 70%,#ececec)}
.product-shot .art{position:absolute;left:65px;top:25px;width:220px;height:230px;background:linear-gradient(135deg,#1a1a1a 0%,#2b2b2b 45%,#1c3fb0 70%,#cfcfcf 100%);border-radius:6px}
.thumbs{left:165px;top:780px;display:grid;grid-template-columns:repeat(4,80px);gap:11px 9px}
.thumb{width:80px;height:78px;border:1px solid var(--line);border-radius:3px;background:linear-gradient(180deg,#fff,#efefef);position:relative}
.thumb .art{position:absolute;left:16px;top:16px;width:46px;height:44px;border-radius:4px}
.thumb.active{border:2px solid #2d6bd0}
.thumb.active::before{content:"";position:absolute;left:36px;top:-8px;border:5px solid transparent;border-bottom-color:#2d6bd0;border-top:0}

/* description */
.section-title{font-family:"Roboto Condensed",sans-serif;font-weight:700;font-size:15.5px;color:var(--blue);white-space:nowrap}
.desc-title{left:530px;top:447px}
.desc{left:532px;top:469px;width:497px;font-size:13px;line-height:19.5px;text-align:justify}
.desc p+p{margin-top:19px}
.feat-title{left:532px;top:662px}
.features{left:532px;top:688px;width:497px;list-style:none;font-size:13px;line-height:19.5px}
.features li{position:relative;padding-left:18px;margin-bottom:8px;text-align:justify}
.features li::before{content:"";position:absolute;left:1px;top:6px;width:8px;height:8px;border-radius:50%;background:#b5b5b5}
.buy-btn{left:532px;top:896px;width:188px;height:51px;background:var(--blue);border-bottom:4px solid var(--blue-dark);font-family:"Open Sans",sans-serif;font-weight:300;font-size:24px;color:var(--white);text-align:center;line-height:50px}

/* footer */
.footer{left:0;top:986px;width:1200px;height:171px;background:var(--footer)}
.footer-base{left:0;top:1157px;width:1200px;height:32px;background:var(--footer-base);font-size:10.5px;color:#aaa;text-align:center;line-height:32px}
.footer-base span{margin:0 4px}
.fcol{top:1000px}
.fcol h4{font-family:"Source Sans 3",sans-serif;font-weight:400;font-size:13px;color:var(--blue);padding-bottom:4px;border-bottom:1px solid #3a3a3a;width:124px}
.fcol ul{list-style:none;margin-top:7px;font-size:12px;color:var(--muted);line-height:24.2px}
.news p{font-size:12px;color:var(--muted);line-height:17.5px;margin-top:8px}
.field{top:1067px;width:114px;height:26px;background:var(--white);font-size:9px;color:#666;padding:8px 10px;font-family:Arial,sans-serif}
.subscribe{left:725px;top:1101px;width:114px;height:30px;background:var(--blue);border-bottom:3px solid var(--blue-dark);color:var(--white);font-size:12.5px;text-align:center;line-height:28px}
.social{left:900px;top:1027px;list-style:none}
.social li{display:flex;align-items:center;gap:10px;height:40px;font-size:12px;color:var(--muted)}
.social i{width:33px;height:33px;border-radius:50%;background:#4a4a4a;display:block}
</style>
</head>
<body>

<div class="abs topbar"></div>
<div class="abs search">Search</div>
<div class="abs search-btn">
  <svg width="25" height="22" viewBox="0 0 25 22"><circle cx="11.5" cy="10" r="5" fill="none" stroke="#fff" stroke-width="2"/><line x1="15" y1="13.5" x2="19" y2="17.5" stroke="#fff" stroke-width="2"/></svg>
</div>
<svg class="abs cart-icon" width="22" height="15" viewBox="0 0 22 15"><path d="M1 5h20l-3 9H4z" fill="#e6b43a"/><path d="M5 5l4-4h6l3 4" fill="none" stroke="#f3d27a" stroke-width="2"/></svg>
<div class="abs cart-text">0 Cart Items</div>

<div class="abs header"></div>
<div class="abs logo">LEARNBOX</div>
<nav class="abs nav"><span>Home</span><span>Connecting</span><span>E-learning Assets</span><span>Content in Motion</span><span>About Us</span><span>Contact Us</span></nav>

<div class="abs hero" role="img" aria-label="Blurred dark background of a classroom behind the headline"></div>
<div class="abs hero-figure" role="img" aria-label="White pictogram of a learner raising a hand"></div>
<h1 class="abs hero-title">Lorem Ipsum is simply dummy text</h1>
<p class="abs hero-text">Lorem Ipsum is simply dummy text of the printing and<br>typesetting industry. Lorem Ipsum has been the industry's<br>standard dummy text ever since the 1500s.</p>
<div class="abs hero-btn">LEARN MORE</div>

<div class="abs tabs">
  <div class="tab active">STORYPATH ASSETS</div>
  <div class="tab">PACKAGES</div>
  <div class="tab">BENEFITS</div>
  <div class="tab">SLIDEDECK LINKAGE</div>
  <div class="tab">ABOUT</div>
</div>
<div class="abs dots"><span class="dot on"></span><span class="dot"></span><span class="dot"></span><span class="dot"></span></div>

<div class="abs product-shot"><div class="art" role="img" aria-label="Product box and disc for a grade 10 engineering graphics course"></div></div>
<div class="abs thumbs">
  <div class="thumb active"><div class="art" role="img" aria-label="Course box and disc" style="background:linear-gradient(135deg,#1a1a1a,#1c3fb0)"></div></div>
  <div class="thumb"><div class="art" role="img" aria-label="Science book with tablet" style="background:linear-gradient(135deg,#8fc25a,#e9e1c8)"></div></div>
  <div class="thumb"><div class="art" role="img" aria-label="Virtual reality headset" style="background:linear-gradient(135deg,#555,#1e1e1e)"></div></div>
  <div class="thumb"><div class="art" role="img" aria-label="Course pack with disc" style="background:linear-gradient(135deg,#f2c531,#3a6ec8)"></div></div>
  <div class="thumb"><div class="art" role="img" aria-label="Desktop computer with lesson" style="background:linear-gradient(135deg,#e26a3a,#cfd6dc)"></div></div>
  <div class="thumb"><div class="art" role="img" aria-label="Tablet with coming soon badge" style="background:linear-gradient(135deg,#f39a2a,#5d6a75)"></div></div>
  <div class="thumb"><div class="art" role="img" aria-label="Science book with tablet" style="background:linear-gradient(135deg,#8fc25a,#e9e1c8)"></div></div>
  <div class="thumb"><div class="art" role="img" aria-label="Virtual reality headset" style="background:linear-gradient(135deg,#555,#1e1e1e)"></div></div>
</div>

<h2 class="abs section-title desc-title">DISCRIPTIVE</h2>
<div class="abs desc">
  <p>Lorem Ipsum is simply dummy text of the printing and typesetting industry. Lorem Ipsum has been the industry's standard dummy text ever since the 1500s, when an unknown printer took a galley of type and scrambled it to make a type specimen book. It has survived not only five centuries, but also the leap into electronic typesetting, remaining essentially unchanged.</p>
  <p>It was popularised in the 1960s with the release of Typeset sheets containing Lorem Ipsum passages, and more recently with desktop publishing software like PageBuilder Pro including versions of Lorem Ipsum.</p>
</div>

<h2 class="abs section-title feat-title">FEATURES OF THE STORYPATH ASSET</h2>
<ul class="abs features">
  <li>Lorem Ipsum is simply dummy text of the printing and typesetting industry. Lorem Ipsum has been the industry's standard dummy text ever since the 1500s,</li>
  <li>Lorem Ipsum is simply dummy text of the printing and typesetting industry.</li>
  <li>Lorem Ipsum is simply dummy text of the printing and typesetting industry. Lorem Ipsum has been the industry's standard dummy text ever since the 1500s,</li>
  <li>Lorem Ipsum is simply dummy text of the printing and typesetting industry.</li>
  <li>Lorem Ipsum is simply dummy text of the printing and typesetting industry.</li>
  <li>Lorem Ipsum is simply dummy text of the printing.</li>
</ul>
<div class="abs buy-btn">Purchase Now</div>

<footer>
  <div class="abs footer"></div>
  <div class="abs fcol" style="left:161px">
    <h4>Quick Links</h4>
    <ul><li>Home</li><li>Connecting learners</li><li>E-learning in Motion</li><li>About Us</li><li>Contact Us</li></ul>
  </div>
  <div class="abs fcol" style="left:381px">
    <h4>Support Links</h4>
    <ul style="padding-left:2px"><li>Legal Notice</li><li>Privacy Policy</li><li>Terms &amp; Conditions</li><li>Help</li></ul>
  </div>
  <div class="abs fcol news" style="left:602px">
    <h4>Newsletter Subscribe</h4>
    <p>Sign-up for our daily emails by entering<br>your information below</p>
  </div>
  <div class="abs field" style="left:603px">Name</div>
  <div class="abs field" style="left:724px">Email Address</div>
  <div class="abs subscribe">Subscribe</div>
  <div class="abs fcol" style="left:902px"><h4 style="width:123px">Social</h4></div>
  <ul class="abs social" style="top:1024px">
    <li><i></i>Friendpage</li>
    <li><i></i>Chirper</li>
    <li><i></i>Circles</li>
  </ul>
  <div class="abs footer-base"><span>© 2013 Company Name.</span><span>Terms of Service</span><span>Privacy</span><span>Sitemap</span></div>
</footer>

</body>
</html>
```